BrookfieldVentures Business Card Design

Design business cards with attached ideas. I am open to several different ideas that would be interesting and innovative. What I have provided is logo and colors. Font should be Helvetica although it could be bold or light as needed. The design can be vertical or horizontal. The design should be more interesting than a standard business card. Files must be ready to send to a printer and in Illustrator format. The text with the five icons should be exact. Send me some ideas and I will get back to you right away. I need to choose a design within 3-5 days.

Target Market(s)

Business audience

Industry/Entity Type

Business

Contact Information for Business Card

Files should be ready to send to printer in illustrator format

Font styles to use
Sans Serif

Colors
3276b5

Requirements
Must have
• Use attached logo and two colors - blue / gray
• Include 5 offering icons and text on back
Nice to have
• Interesting and innovative design. Vertical or horizontal are both fine.

```html
<!DOCTYPE html>
<html lang="en">
<head>
<meta charset="utf-8">
<title>BrookfieldVentures Business Card</title>
<link href="https://fonts.googleapis.com/css2?family=Arimo:wght@400;700&display=swap" rel="stylesheet">
<style>
  :root {
    --backdrop: #4b3424;
    --card: #ffffff;
    --brand-blue: #1f5a8e;
    --ink: #1c1c1c;
    --ink-soft: #2e2e2e;
    --gray: #3a3d42;
  }
  * { margin: 0; padding: 0; box-sizing: border-box; }
  html, body { width: 1200px; height: 1000px; overflow: hidden; }
  body {
    position: relative;
    background: var(--backdrop);
    font-family: "Arimo", Helvetica, Arial, sans-serif;
    color: var(--ink);
  }
  .card {
    position: absolute;
    left: 287px;
    width: 626px;
    height: 367px;
    background: var(--card);
    border-radius: 14px;
    border: 1px solid #222;
  }
  .card--front { top: 120px; }
  .card--back { top: 512px; }

  .brand-mark {
    position: absolute;
    left: 116px; top: 20px;
    width: 87px; height: 87px;
    background: var(--brand-blue);
    border-radius: 5px;
  }
  .brand-name {
    position: absolute;
    left: 19px; top: 126px;
    font-size: 37px;
    font-weight: 400;
    color: var(--brand-blue);
    letter-spacing: -0.3px;
  }
  .tagline {
    position: absolute;
    left: 42px; top: 168px;
    font-size: 16px;
    color: var(--ink);
  }
  .contact {
    position: absolute;
    right: 27px; top: 188px;
    text-align: right;
    color: var(--ink);
  }
  .contact__name { font-size: 21px; line-height: 24px; }
  .contact__suffix { font-size: 18px; }
  .contact__title { font-size: 18px; line-height: 24px; }
  .contact__details { margin-top: 26px; font-size: 18px; line-height: 30px; color: var(--ink-soft); }

  .offerings-title {
    position: absolute;
    left: 171px; top: 30px;
    font-size: 18px;
    color: var(--ink);
  }
  .offerings-title__brand { color: var(--brand-blue); }
  .offerings {
    position: absolute;
    left: 114px; top: 72px;
    list-style: none;
  }
  .offering {
    display: flex;
    align-items: center;
    height: 44px;
    margin-bottom: 10.5px;
    font-size: 16px;
    color: var(--ink-soft);
  }
  .offering__icon { width: 44px; height: 44px; margin-right: 13px; flex: none; }
  .offering__label { color: var(--ink); }
</style>
</head>
<body>

<section class="card card--front">
  <div class="brand-mark"></div>
  <div class="brand-name">BrookfieldVentures</div>
  <div class="tagline">Twice the Value - Half the Cost</div>
  <div class="contact">
    <div class="contact__name">Dana Whitlock, <span class="contact__suffix">PhD</span></div>
    <div class="contact__title">Managing Director</div>
    <div class="contact__details">
      <div>555-014-2273</div>
      <div>Dana@BrookfieldVentures.com</div>
      <div>BrookfieldVentures.com</div>
    </div>
  </div>
</section>

<section class="card card--back">
  <div class="offerings-title"><span class="offerings-title__brand">BrookfieldVentures</span> Offerings</div>
  <ul class="offerings">
    <li class="offering">
      <svg class="offering__icon" viewBox="0 0 44 44"><circle cx="22" cy="22" r="22" fill="var(--brand-blue)"/><rect x="12" y="13" width="20" height="18" fill="none" stroke="#fff" stroke-width="2"/><rect x="15" y="16" width="5" height="5" fill="#fff"/><path d="M22 17h7M22 20h7M15 24h14M15 27h14" stroke="#fff" stroke-width="1.5"/></svg>
      <span><span class="offering__label">Concepts:</span> Thought leadership white papers</span>
    </li>
    <li class="offering">
      <svg class="offering__icon" viewBox="0 0 44 44"><circle cx="22" cy="22" r="22" fill="var(--brand-blue)"/><circle cx="22" cy="15" r="4" fill="#fff"/><path d="M15 26a7 6 0 0 1 14 0z" fill="#fff"/><rect x="11" y="27" width="22" height="3" fill="#fff"/></svg>
      <span><span class="offering__label">Curriculum:</span> Short courses on strategy</span>
    </li>
    <li class="offering">
      <svg class="offering__icon" viewBox="0 0 44 44"><circle cx="22" cy="22" r="22" fill="var(--brand-blue)"/><circle cx="12" cy="14" r="3" fill="#fff"/><rect x="9" y="18" width="6" height="12" rx="1" fill="#fff"/><circle cx="32" cy="14" r="3" fill="#fff"/><rect x="29" y="18" width="6" height="12" rx="1" fill="#fff"/><path d="M18 19h8l-2-2M26 24h-8l2 2" stroke="#fff" stroke-width="1.5" fill="none"/></svg>
      <span><span class="offering__label">Couching:</span> Building your strategic leadership</span>
    </li>
    <li class="offering">
      <svg class="offering__icon" viewBox="0 0 44 44"><circle cx="22" cy="22" r="22" fill="var(--brand-blue)"/><circle cx="22" cy="22" r="8" fill="none" stroke="#fff" stroke-width="1.5" stroke-dasharray="2 2"/><circle cx="22" cy="13" r="3" fill="#fff"/><circle cx="14" cy="28" r="3" fill="#fff"/><circle cx="30" cy="28" r="3" fill="#fff"/></svg>
      <span><span class="offering__label">Consulting:</span> Developing your strategic future</span>
    </li>
    <li class="offering">
      <svg class="offering__icon" viewBox="0 0 44 44"><circle cx="22" cy="22" r="22" fill="var(--brand-blue)"/><circle cx="12" cy="14" r="3" fill="#fff"/><rect x="9" y="18" width="6" height="13" rx="1" fill="#fff"/><rect x="19" y="12" width="15" height="11" fill="none" stroke="#fff" stroke-width="1.5"/><path d="M21 20l4-3 3 2 4-4" stroke="#fff" stroke-width="1.5" fill="none"/></svg>
      <span><span class="offering__label">ScoreCard:</span> Balanced ScoreCard and software</span>
    </li>
  </ul>
</section>

</body>
</html>
```